QVAR Individual and Corporate Development Business Card Design

QVAR needs a business card design that is aligned with it's values and targetted markets. Harmonic Lattice of Cognition Network's self diagnosis model and tools, which can be used for personal improvement and team/business performance enhancement, is based on the learnings of over 20 years of medical practitioning. QVAR supercharges personal effectiveness and awareness to also increase team and business performance.

The targetted markets are high performance individuals and teams who aspire seek to enhance their capabilities and achieve their absolute best potential.

Look and feel for the business card design we are looking for is high technology, premium, fresh, new and medical.

Target Market(s)

Industry/Entity Type

Business Consultant

Contact Information for Business Card

Logo, Full Name, Title, Phone number, Email, company name, Address,

Font styles to use
Sans Serif

Requirements
Must have
• Tag line: Maximising Performance for Highly Effective People
• Please use same colours as the logo.

```html
<!DOCTYPE html>
<html lang="en">
<head>
<meta charset="utf-8">
<title>QVAR Business Card</title>
<link href="https://fonts.googleapis.com/css2?family=Open+Sans:wght@400;600;700&family=Oswald:wght@500&display=swap" rel="stylesheet">
<style>
  :root {
    --stage: #1c1d1f;
    --card-dark-a: #0a0f13;
    --card-dark-b: #17212a;
    --cyan: #1fb4c9;
    --grey-line: #7c858c;
    --grey-text: #8a8f93;
    --grey-light: #b7bcc0;
    --paper: #ffffff;
    --ink: #5b6166;
  }
  * { box-sizing: border-box; margin: 0; padding: 0; }
  html, body { width: 1200px; height: 1200px; overflow: hidden; }
  body {
    background: var(--stage);
    font-family: "Open Sans", sans-serif;
    display: flex;
    flex-direction: column;
    align-items: center;
    justify-content: center;
    gap: 44px;
  }
  .card {
    width: 900px;
    height: 514px;
    position: relative;
    box-shadow: 0 18px 40px rgba(0,0,0,.55);
  }
  /* Front */
  .card-front {
    background: radial-gradient(ellipse at 50% 40%, var(--card-dark-b), var(--card-dark-a) 75%);
    display: flex;
    flex-direction: column;
    align-items: center;
    justify-content: center;
  }
  .brand-row { display: flex; align-items: center; gap: 22px; }
  .brand-dot {
    width: 46px; height: 46px; border-radius: 50%;
    background: var(--cyan);
  }
  .brand-name {
    font-weight: 700;
    font-size: 120px;
    line-height: 1;
    letter-spacing: 6px;
    color: var(--cyan);
  }
  .brand-rule {
    width: 500px; height: 2px;
    background: var(--grey-line);
    margin: 20px 0 14px;
  }
  .brand-full {
    font-weight: 600;
    font-size: 21px;
    letter-spacing: 2.5px;
    text-transform: uppercase;
    color: var(--cyan);
    text-align: center;
    line-height: 1.35;
  }
  .tagline {
    margin-top: 26px;
    font-size: 17px;
    font-weight: 400;
    letter-spacing: 1px;
    color: var(--grey-light);
    text-align: center;
  }
  /* Back */
  .card-back { background: var(--paper); }
  .identity {
    position: absolute;
    left: 290px; top: 190px;
    text-align: right;
    width: 260px;
  }
  .person-name {
    font-family: "Oswald", sans-serif;
    font-weight: 500;
    font-size: 42px;
    color: var(--cyan);
    text-transform: uppercase;
    line-height: 1.05;
  }
  .person-title { font-size: 20px; color: var(--grey-text); }
  .divider {
    position: absolute;
    left: 572px; top: 180px;
    width: 2px; height: 96px;
    background: var(--ink);
    opacity: .7;
  }
  .contact-list {
    position: absolute;
    left: 594px; top: 178px;
    list-style: none;
  }
  .contact-list li {
    display: flex; align-items: center; gap: 12px;
    font-size: 19px; color: var(--ink);
    line-height: 33px;
  }
  .contact-list svg { width: 16px; height: 16px; fill: var(--cyan); flex: none; }
  .address {
    position: absolute;
    right: 70px; bottom: 70px;
    font-size: 19px; color: var(--ink);
  }
</style>
</head>
<body>
  <section class="card card-front">
    <div class="brand-row">
      <span class="brand-dot"></span>
      <span class="brand-name">QVAR</span>
    </div>
    <div class="brand-rule"></div>
    <p class="brand-full">Harmonic Lattice<br>of Cognition Network</p>
    <p class="tagline">Maximising Performance for Highly Effective People</p>
  </section>

  <section class="card card-back">
    <div class="identity">
      <p class="person-name">Daniel Reyes</p>
      <p class="person-title">General Manager</p>
    </div>
    <div class="divider"></div>
    <ul class="contact-list">
      <li>
        <svg viewBox="0 0 16 16"><path d="M3.2 1.5l2.3 2.6-1.3 1.6c.9 2 2.3 3.4 4.2 4.3l1.6-1.3 2.6 2.2-1.2 2.2C6.5 13.8 2.2 9.5 1.1 2.7z"/></svg>
        555-0142-7788
      </li>
      <li>
        <svg viewBox="0 0 16 16"><path d="M1 3.5h14L8 8.8zM1 5.2l7 5.2 7-5.2V13H1z"/></svg>
        info@qvarnetwork.com
      </li>
      <li>
        <svg viewBox="0 0 16 16"><path d="M8 1a7 7 0 100 14A7 7 0 008 1zm0 1.4c.8.8 1.4 2.2 1.6 3.8H6.4C6.6 4.6 7.2 3.2 8 2.4zM2.5 7.4h2.6c0 .4 0 .8.1 1.2H2.5a5.6 5.6 0 010-1.2zm3.9 2.4h3.2C9.4 11.4 8.8 12.8 8 13.6c-.8-.8-1.4-2.2-1.6-3.8zm4.5-2.4h2.6a5.6 5.6 0 010 1.2h-2.6c.1-.4.1-.8 0-1.2zm-4.5 0h3.2v1.2H6.4z"/></svg>
        www.qvarnetwork.com
      </li>
    </ul>
    <p class="address">18 Linden Court, Harbor Row P.O. Box 204, 310 Avenue</p>
  </section>
</body>
</html>
```